Hollow Fern Kentucky Bourbon Whiskey

We need a label design for a bottle of whiskey. It is for a 750 ml bottle and needs to have a place to write in proof, age, and bottle number at bottom of label. It is a single barrel bourbon. We want to include our tree logo attached in the upload files in some way. Leave out the Distillery part to where it just says Hollow Fern Bourbon Whiskey with the tree. We need the label to be clean and modern. I have also attached a picture of the bottle the label is intended to go on.

Industry/Entity Type

Bourbon

Requirements
Must have
• Hollow Fern tree from file

```html
<!DOCTYPE html>
<html lang="en">
<head>
<meta charset="utf-8">
<title>Hollow Fern Kentucky Bourbon Whiskey – Label</title>
<link href="https://fonts.googleapis.com/css2?family=Cinzel:wght@500&family=Rye&family=Alfa+Slab+One&family=Barlow+Condensed:wght@500;600&display=swap" rel="stylesheet">
<style>
  :root {
    --backdrop: #000000;
    --gold-edge: #e2c46e;
    --gold-edge-dark: #c9a64d;
    --gold-left: #e9c54a;
    --gold-shine: #fffbd8;
    --amber: #e4a33a;
    --cask-brown: #8a4a35;
    --ink: #22150f;
    --ink-brown: #4a2c1f;
    --rule: #1a100b;
  }
  html, body {
    margin: 0;
    width: 1200px;
    height: 1000px;
    overflow: hidden;
    background: var(--backdrop);
  }
  .canvas {
    position: relative;
    width: 1200px;
    height: 1000px;
  }
  .label-shape {
    position: absolute;
    inset: 0;
  }
  .label-content {
    position: absolute;
    inset: 0;
    color: var(--ink);
  }
  .centered {
    position: absolute;
    left: 362px;
    width: 478px;
    text-align: center;
    margin: 0;
  }
  .brand-mark {
    position: absolute;
    left: 566px;
    top: 178px;
    width: 68px;
    height: 68px;
    border-radius: 50%;
    background: var(--ink-brown);
  }
  .brand-name {
    top: 284px;
    font-family: "Cinzel", serif;
    font-weight: 500;
    font-size: 29px;
    letter-spacing: 0.5px;
    line-height: 1;
  }
  .brand-sub {
    top: 321px;
    font-family: "Cinzel", serif;
    font-weight: 500;
    font-size: 17px;
    letter-spacing: 1.5px;
    line-height: 1;
  }
  .product-line {
    font-family: "Alfa Slab One", serif;
    font-size: 34px;
    letter-spacing: 9px;
    line-height: 1;
    padding-left: 9px;
  }
  .product-origin { top: 404px; }
  .product-type {
    top: 456px;
    font-family: "Rye", serif;
    font-size: 66px;
    letter-spacing: 3px;
    line-height: 1;
    color: var(--ink-brown);
    -webkit-text-stroke: 1.5px var(--ink);
  }
  .product-spirit { top: 557px; }
  .field-label {
    position: absolute;
    font-family: "Barlow Condensed", sans-serif;
    font-weight: 500;
    font-size: 17px;
    line-height: 1;
    text-transform: uppercase;
  }
  .field-proof { left: 438px; top: 665px; }
  .field-bottle { left: 615px; top: 665px; }
  .field-age { left: 438px; top: 706px; }
  .spec {
    position: absolute;
    top: 793px;
    font-family: "Barlow Condensed", sans-serif;
    font-weight: 500;
    font-size: 18px;
    line-height: 1;
  }
  .spec-abv { left: 466px; }
  .spec-volume { left: 654px; }
  .barrel-art {
    position: absolute;
    left: 568px;
    top: 758px;
    width: 64px;
    height: 82px;
    border-radius: 30px 30px 6px 6px;
    background: linear-gradient(180deg, #b27a3c, #6b4424);
  }
  .web-address {
    top: 862px;
    font-family: "Barlow Condensed", sans-serif;
    font-weight: 600;
    font-size: 14px;
    letter-spacing: 2.2px;
    line-height: 1;
  }
</style>
</head>
<body>
<main class="canvas">
  <svg class="label-shape" width="1200" height="1000" viewBox="0 0 1200 1000" aria-hidden="true">
    <defs>
      <linearGradient id="label-face" x1="376" y1="0" x2="826" y2="0" gradientUnits="userSpaceOnUse">
        <stop offset="0" stop-color="var(--gold-left)"/>
        <stop offset="0.22" stop-color="#f4e07a"/>
        <stop offset="0.5" stop-color="var(--gold-shine)"/>
        <stop offset="0.66" stop-color="#f1c766"/>
        <stop offset="0.74" stop-color="var(--amber)"/>
        <stop offset="0.8" stop-color="#b8763a"/>
        <stop offset="0.84" stop-color="var(--cask-brown)"/>
        <stop offset="1" stop-color="var(--cask-brown)"/>
      </linearGradient>
      <linearGradient id="label-edge" x1="0" y1="128" x2="0" y2="903" gradientUnits="userSpaceOnUse">
        <stop offset="0" stop-color="var(--gold-edge)"/>
        <stop offset="0.5" stop-color="var(--gold-edge-dark)"/>
        <stop offset="1" stop-color="var(--gold-edge)"/>
      </linearGradient>
    </defs>
    <path class="label-border" fill="url(#label-edge)"
      d="M362 212 A54 54 0 0 0 416 158 L426 158 Q440 128 482 128 L718 128 Q760 128 774 158 L786 158 A54 54 0 0 0 840 212 L840 850 A53 53 0 0 0 787 903 L415 903 A53 53 0 0 0 362 850 Z"/>
    <path class="label-face" fill="url(#label-face)" stroke="#8a6a2a" stroke-width="1"
      d="M376 224 A52 52 0 0 0 428 172 L436 172 Q450 142 488 142 L712 142 Q750 142 764 172 L772 172 A52 52 0 0 0 824 224 L824 838 A51 51 0 0 0 773 889 L427 889 A51 51 0 0 0 376 838 Z"/>
    <g class="name-rules" stroke="var(--rule)" stroke-width="2">
      <line x1="478" y1="332" x2="528" y2="332"/>
      <line x1="672" y1="332" x2="724" y2="332"/>
    </g>
    <g class="record-form" stroke="var(--rule)">
      <line x1="437" y1="650" x2="763" y2="650" stroke-width="3"/>
      <line x1="437" y1="691" x2="587" y2="691" stroke-width="2"/>
      <line x1="615" y1="691" x2="763" y2="691" stroke-width="2"/>
      <line x1="600" y1="667" x2="600" y2="716" stroke-width="2"/>
      <line x1="437" y1="735" x2="763" y2="735" stroke-width="3"/>
    </g>
  </svg>

  <div class="label-content">
    <span class="brand-mark" aria-hidden="true"></span>
    <p class="centered brand-name">HOLLOW FERN</p>
    <p class="centered brand-sub">DISTILLERY</p>

    <p class="centered product-line product-origin">KENTUCKY</p>
    <p class="centered product-type">BOURBON</p>
    <p class="centered product-line product-spirit">WHISKEY</p>

    <span class="field-label field-proof">Proof</span>
    <span class="field-label field-bottle">Bottle N°</span>
    <span class="field-label field-age">Age</span>

    <span class="spec spec-abv">Alc.45%.</span>
    <div class="barrel-art" role="img" aria-label="Engraved illustration of an oak whiskey barrel on a stand"></div>
    <span class="spec spec-volume">750ml</span>

    <p class="centered web-address">www.hollowfernspirits.com</p>
  </div>
</main>
</body>
</html>
```